Tool kit box label .

Looking for a label design to attach to our engine tool kit, will have logo design included for brand KRONVALE TOOLS . Label also to have this text : Fuel Injection pump kit .
The sticker will be put on the packages shown in attachments.
Target Market(s)
Automotive workshops
Colors
fece3e
1b1b1b
Requirements
Must have
- Cool industrial look

```html
<!DOCTYPE html>
<html lang="en">
<head>
<meta charset="utf-8">
<title>Fuel Injection Pump Kit – Label</title>
<link rel="stylesheet" href="https://fonts.googleapis.com/css2?family=Barlow+Condensed:ital,wght@1,800&family=Montserrat:wght@800&display=swap">
<style>
  :root {
    --page-bg: #0b0f17;
    --amber: #fece3e;
    --amber-deep: #f7a516;
    --amber-glow: #ffd84d;
    --ink: #1b1b1b;
    --band-edge: #8f8f8f;
  }
  html, body {
    margin: 0;
    width: 1200px;
    height: 1200px;
    overflow: hidden;
    background: var(--page-bg);
  }
  .label {
    position: absolute;
    left: 60px;
    top: 300px;
    width: 1080px;
    height: 600px;
    border-radius: 46px;
    overflow: hidden;
    background: radial-gradient(ellipse at 45% 55%, var(--amber-glow) 0%, var(--amber) 35%, var(--amber-deep) 100%);
  }
  .label__band {
    position: absolute;
    inset: 0;
    width: 1080px;
    height: 600px;
  }
  .label__title {
    position: absolute;
    left: 106px;
    top: 88px;
    margin: 0;
    font-family: "Barlow Condensed", sans-serif;
    font-style: italic;
    font-weight: 800;
    font-size: 80px;
    line-height: 0.96;
    letter-spacing: -0.5px;
    color: var(--ink);
    text-transform: uppercase;
    z-index: 2;
  }
  .label__brand {
    position: absolute;
    left: 98px;
    top: 468px;
    font-family: "Montserrat", sans-serif;
    font-weight: 800;
    font-size: 27px;
    letter-spacing: 0.5px;
    color: var(--ink);
    padding-bottom: 4px;
    border-bottom: 2px solid var(--ink);
  }
  .label__engine {
    position: absolute;
    left: 590px;
    top: 100px;
    width: 340px;
    height: 390px;
    background: radial-gradient(closest-side, #3a3a3a 0%, #1f1f1f 70%, rgba(31,31,31,0) 100%);
  }
</style>
</head>
<body>
  <div class="label">
    <svg class="label__band" viewBox="0 0 1080 600" aria-hidden="true">
      <defs>
        <linearGradient id="bandShade" x1="0" y1="0" x2="1" y2="0">
          <stop offset="0" stop-color="#1e1e1e"/>
          <stop offset="0.5" stop-color="#4a4a4a"/>
          <stop offset="1" stop-color="#1e1e1e"/>
        </linearGradient>
      </defs>
      <polygon points="760,0 1050,0 800,600 486,600" fill="var(--band-edge)"/>
      <polygon points="774,0 1037,0 787,600 500,600" fill="url(#bandShade)"/>
    </svg>

    <h1 class="label__title">Fuel Injection<br>Pump Kit</h1>

    <div class="label__engine" role="img" aria-label="Photograph of a compact diesel engine"></div>

    <div class="label__brand">KRONVALE TOOLS</div>
  </div>
</body>
</html>
```